Business Card Design for Mortgage Broking Business

We need to redesign the business card. Mortgage broking business, doing home loan and commercial loans, existing logo, also RQTB member logo. design style needs to be simple, professional, elegant.

once final, need to setup for a team of different names and contact details.

Industry/Entity Type

Loan

Contact Information for Business Card

Name; Mobile; Email; Address; Tel; Fax; Australian Credit Licence: 618204

```html
<!DOCTYPE html>
<html lang="en">
<head>
<meta charset="utf-8">
<title>Keystone Home Lending – Business Card</title>
<link rel="stylesheet" href="https://fonts.googleapis.com/css2?family=Lato:wght@400;700;900&family=Questrial&display=swap">
<style>
  :root {
    --stage: #2e2e2e;
    --card: #ffffff;
    --navy: #232a86;
    --sky: #1f9bd7;
    --ink: #1c1c1c;
    --violet-soft: #aaa9d9;
    --green-soft: #9fd9a8;
    --badge: #3b5a8c;
  }
  * { box-sizing: border-box; margin: 0; padding: 0; }
  html, body { width: 1200px; height: 873px; overflow: hidden; }
  body {
    background: var(--stage);
    position: relative;
    font-family: "Lato", sans-serif;
  }
  .card {
    position: absolute;
    width: 520px;
    height: 300px;
    background: var(--card);
    border-radius: 22px;
    overflow: hidden;
  }
  .card--front { left: 50px; top: 170px; }
  .card--back { left: 630px; top: 400px; }

  .brand-name {
    font-family: "Lato", sans-serif;
    font-weight: 900;
    color: var(--navy);
    font-size: 22px;
    line-height: 1.1;
    display: flex;
    align-items: center;
    gap: 8px;
  }
  .brand-name .brand-square {
    width: 16px; height: 16px; background: var(--navy);
  }

  /* front */
  .card--front .brand-name { position: absolute; left: 40px; top: 132px; }
  .front-decor {
    position: absolute;
    right: 0; top: 0;
    width: 250px; height: 300px;
    background: linear-gradient(180deg, var(--violet-soft) 0%, #c8dbe0 50%, var(--green-soft) 100%);
    opacity: 0.75;
    clip-path: polygon(30% 0, 100% 0, 100% 100%, 0 100%, 30% 55%);
  }
  .member-badge {
    position: absolute;
    right: 30px; bottom: 70px;
    width: 92px; height: 40px;
    background: #fff;
    border: 2px solid var(--badge);
  }

  /* back */
  .card--back .brand-name { position: absolute; right: 34px; top: 30px; }
  .divider {
    position: absolute;
    left: 230px; top: 140px;
    width: 260px; height: 3px;
    display: flex;
  }
  .divider .divider-dark { flex: 0 0 62%; background: var(--navy); }
  .divider .divider-light { flex: 1; background: var(--sky); margin-left: 4px; }
  .person { position: absolute; left: 32px; top: 124px; }
  .person-name {
    font-family: "Questrial", sans-serif;
    font-weight: 700;
    font-size: 27px;
    color: var(--navy);
    letter-spacing: 0.2px;
    -webkit-text-stroke: 0.6px var(--navy);
  }
  .person-title {
    font-family: "Questrial", sans-serif;
    font-size: 13px;
    color: var(--sky);
    margin-top: -2px;
  }
  .contact-list {
    position: absolute;
    left: 32px; top: 186px;
    list-style: none;
    font-size: 13px;
    color: var(--navy);
  }
  .contact-list li {
    display: flex; align-items: center; gap: 8px;
    height: 19px;
  }
  .contact-list svg { width: 11px; height: 11px; fill: var(--sky); flex: none; }
  .website {
    position: absolute;
    left: 32px; top: 266px;
    font-weight: 900;
    font-size: 15px;
    color: var(--ink);
  }
  .address {
    position: absolute;
    right: 34px; top: 188px;
    text-align: right;
    font-size: 13px;
    line-height: 1.35;
    color: var(--navy);
  }
</style>
</head>
<body>

<section class="card card--front" aria-label="Card front">
  <div class="brand-name"><span class="brand-square"></span>Keystone Home Lending</div>
  <div class="front-decor" role="img" aria-label="Faint tiled brand decoration in violet and green"></div>
  <div class="member-badge" role="img" aria-label="Association membership badge"></div>
</section>

<section class="card card--back" aria-label="Card back">
  <div class="brand-name"><span class="brand-square"></span>Keystone Home Lending</div>

  <div class="divider"><span class="divider-dark"></span><span class="divider-light"></span></div>

  <div class="person">
    <h1 class="person-name">Daniel Marsh</h1>
    <p class="person-title">Customer Relations Director</p>
  </div>

  <ul class="contact-list">
    <li>
      <svg viewBox="0 0 12 12" aria-hidden="true"><path d="M3 0h6a1 1 0 0 1 1 1v10a1 1 0 0 1-1 1H3a1 1 0 0 1-1-1V1a1 1 0 0 1 1-1zm0 1.5v8h6v-8z"/></svg>
      +41 70 555 0182
    </li>
    <li>
      <svg viewBox="0 0 12 12" aria-hidden="true"><path d="M1 3c0-1 1-2 5-2s5 1 5 2v1H8V3H4v1H1zM3 5h6l2 6H1z"/></svg>
      +41 20 555 0147
    </li>
    <li>
      <svg viewBox="0 0 12 12" aria-hidden="true"><path d="M3 0h6v3H3zM1 4h10v5H9v3H3V9H1zm3 4v3h4V8z"/></svg>
      +41 20 555 0193
    </li>
    <li>
      <svg viewBox="0 0 12 12" aria-hidden="true"><path d="M0 2h12v8H0zm1 1v.5l5 3 5-3V3z"/></svg>
      daniel@keystonehomelending.com
    </li>
  </ul>

  <p class="website">www.keystonehomelending.com</p>

  <address class="address" style="font-style: normal;">
    28 harbour lane, west mill road,<br>Canada.
  </address>
</section>

</body>
</html>
```